11 x 11 Flyer Design for Social Media - Reverse Mortgages

62 or older?

A Reverse Mortgage
could be
Your Road to Financial Freedom

* No Monthly Payments
* No Income Requirements
* No Credit Score Requirements
* No Loss of Ownership

Receive cash by lump sum, monthly installments or a line of credit!!

Call us today for a Free Consultation!!
(800) 471-2965

Bluegate Financial Services, Inc.
NMLS #318760
www.bluegatehome.com

```html
<!DOCTYPE html>
<html lang="en">
<head>
<meta charset="utf-8">
<title>Reverse Mortgage Flyer</title>
<link href="https://fonts.googleapis.com/css2?family=Montserrat:wght@600;700;800&display=swap" rel="stylesheet">
<style>
  :root {
    --brand-blue: #1b5fa8;
    --sand: #d5cb92;
    --gold-line: #d8cd94;
    --ink: #111111;
    --paper: #ffffff;
  }
  * { margin: 0; padding: 0; box-sizing: border-box; }
  html, body { width: 1200px; height: 1199px; overflow: hidden; background: var(--paper); }
  .flyer {
    position: relative; width: 1200px; height: 1199px; overflow: hidden;
    font-family: "Montserrat", Arial, sans-serif; background: var(--paper);
  }
  .flyer svg.backdrop { position: absolute; left: 0; top: 0; }
  .age-question {
    position: absolute; left: 397px; top: 50px;
    font-size: 94px; font-weight: 700; line-height: 95px; color: var(--ink);
    letter-spacing: -0.5px;
  }
  .headline {
    position: absolute; left: 52px; top: 650px;
    font-size: 54px; font-weight: 800; line-height: 58px; color: var(--brand-blue);
    text-transform: uppercase; letter-spacing: 0.6px;
  }
  .benefits { position: absolute; left: 52px; top: 890px; list-style: none; }
  .benefits li {
    position: relative; padding-left: 42px;
    font-size: 33px; font-weight: 700; line-height: 43px; color: var(--ink);
  }
  .benefits li::before {
    content: ""; position: absolute; left: 1px; top: 14px;
    width: 16px; height: 16px; background: var(--brand-blue);
  }
  .brand-box {
    position: absolute; left: 749px; top: 629px; width: 411px; height: 254px;
    display: flex; flex-direction: column; align-items: center; justify-content: center; gap: 18px;
    text-align: center;
  }
  .brand-box .mark { width: 78px; height: 78px; border-radius: 50%; background: var(--brand-blue); }
  .brand-box .brand-name { font-size: 30px; font-weight: 700; line-height: 36px; color: var(--brand-blue); }
  .contact {
    position: absolute; left: 749px; top: 893px; width: 430px; text-align: center;
    font-size: 20px; font-weight: 600; line-height: 40px; color: var(--ink);
  }
  .cta {
    position: absolute; left: 0; top: 1085px; width: 1200px; text-align: center;
    font-size: 29.5px; font-weight: 700; color: var(--brand-blue); letter-spacing: 0.8px;
  }
  .payout-band {
    position: absolute; left: 0; top: 1130px; width: 1200px; height: 69px;
    background: var(--brand-blue); color: var(--paper);
    display: flex; align-items: center; justify-content: center;
    font-size: 31px; font-weight: 700;
  }
</style>
</head>
<body>
<div class="flyer">
  <svg class="backdrop" width="1200" height="1199" viewBox="0 0 1200 1199">
    <defs>
      <radialGradient id="autumnGlow" cx="0.72" cy="0.55" r="0.75">
        <stop offset="0" stop-color="#c9b48a"/>
        <stop offset="0.35" stop-color="#e2c27a"/>
        <stop offset="0.7" stop-color="#efd690"/>
        <stop offset="1" stop-color="#c8a456"/>
      </radialGradient>
      <linearGradient id="indoorGlow" x1="0" y1="0" x2="0.4" y2="1">
        <stop offset="0" stop-color="#ebe7de"/>
        <stop offset="0.45" stop-color="#a9a48e"/>
        <stop offset="1" stop-color="#3f4a36"/>
      </linearGradient>
      <linearGradient id="parkGlow" x1="0" y1="0" x2="1" y2="0.6">
        <stop offset="0" stop-color="#f4f1e2"/>
        <stop offset="0.4" stop-color="#8c7658"/>
        <stop offset="0.75" stop-color="#d9cfb8"/>
        <stop offset="1" stop-color="#c7c08f"/>
      </linearGradient>
    </defs>
    <rect class="top-field" x="0" y="0" width="1200" height="603" fill="var(--gold-line)"/>
    <polygon points="0,0 225,0 394,305 0,305" fill="url(#indoorGlow)" role="img" aria-label="Photo of a smiling older man seated at a table"/>
    <rect x="0" y="314" width="396" height="15" fill="var(--brand-blue)"/>
    <polygon points="0,342 415,342 551,587 0,587" fill="url(#parkGlow)" role="img" aria-label="Photo of a smiling older woman with headphones holding a phone beside a tree"/>
    <polygon points="262,0 1200,0 1200,587 597,587" fill="url(#autumnGlow)" role="img" aria-label="Photo of a happy older couple embracing outdoors in autumn light"/>
    <polygon points="232,0 252,0 578,603 558,603" fill="var(--brand-blue)"/>
    <rect x="0" y="587" width="1200" height="16" fill="var(--brand-blue)"/>
    <polygon class="info-panel" points="0,629 603,629 749,883 1200,883 1200,1130 0,1130" fill="var(--sand)"/>
    <rect class="brand-field" x="749" y="629" width="411" height="254" fill="var(--paper)"/>
  </svg>

  <h1 class="age-question">62 or<br>Older?</h1>

  <h2 class="headline">A Reverse<br>Mortgage Could<br>Be Your Road To<br>Financial Freedom</h2>

  <ul class="benefits">
    <li>No Monthly Payments</li>
    <li>No Income Requirements</li>
    <li>No Credit Score Requirements</li>
    <li>No Loss of Ownership</li>
  </ul>

  <div class="brand-box">
    <span class="mark"></span>
    <span class="brand-name">Bluegate<br>Financial Services, Inc.</span>
  </div>

  <div class="contact">
    <p>Bluegate Financial Services, Inc.</p>
    <p>NMLS #318760</p>
    <p>www.bluegatehome.com</p>
  </div>

  <p class="cta">CALL US TODAY FOR A FREE CONSULTATION!! (800) 471-2965</p>

  <p class="payout-band">Receive cash by lump sum, monthly installments or a line of credit!!</p>
</div>
</body>
</html>
```